new business card, with new logo. Looking for full design

I would like to have a graphic designer/artist create a high standard, premium business logo and business card design that I can either use to print on my own or have printed through them as well. Also, would be nice if I could customize with new employee names and info afterwards. Also, though I don't have a logo, something that matches the theme here https://veridanstrategy.com/ as well as incorporates the letter "M" is what I am currently thinking. Thanks!

Target Market(s)

High end corporate executives

Industry/Entity Type

Economics

Contact Information for Business Card

Dr. Tomas Ruelle-Brandt
Principal Advisor
TRB@VeridanStrategy.com
other contact/website details from here: https://veridanstrategy.com/

Logo Text

Veridan Strategy Group

```html
<!DOCTYPE html>
<html lang="en">
<head>
<meta charset="utf-8">
<title>Veridan Strategy Group — Business Card</title>
<link href="https://fonts.googleapis.com/css2?family=Montserrat:wght@400;500;600;700&display=swap" rel="stylesheet">
<style>
  :root {
    --backdrop: #d1d1cc;
    --card-white: #ffffff;
    --card-black: #000000;
    --ink: #111111;
    --ink-soft: #7a7a7a;
    --paper-text: #ffffff;
  }
  * { box-sizing: border-box; margin: 0; padding: 0; }
  html, body {
    width: 1200px;
    height: 801px;
    overflow: hidden;
    background: var(--backdrop);
    font-family: "Montserrat", sans-serif;
  }
  .stage {
    position: relative;
    width: 1200px;
    height: 801px;
    display: flex;
    align-items: center;
    justify-content: center;
    gap: 40px;
  }
  .card {
    position: relative;
    width: 520px;
    height: 297px;
    box-shadow: 0 6px 18px rgba(0,0,0,0.18);
  }

  /* Front */
  .card-front {
    background: var(--card-white);
    color: var(--ink);
  }
  .front-brand {
    position: absolute;
    top: 40px;
    left: 190px;
  }
  .identity {
    position: absolute;
    left: 40px;
    top: 114px;
  }
  .identity .name {
    font-weight: 700;
    font-size: 22px;
    letter-spacing: 0.4px;
    line-height: 1.1;
    text-transform: uppercase;
    white-space: nowrap;
  }
  .identity .role {
    font-weight: 400;
    font-size: 12.5px;
    color: var(--ink-soft);
    margin-top: 4px;
  }
  .rule {
    position: absolute;
    left: 40px;
    right: 40px;
    top: 168px;
    height: 1px;
    background: var(--ink);
  }
  .contacts {
    position: absolute;
    left: 40px;
    top: 184px;
    list-style: none;
  }
  .contacts li {
    display: flex;
    align-items: center;
    gap: 10px;
    font-size: 12.5px;
    color: var(--ink-soft);
    height: 22px;
    white-space: nowrap;
  }
  .contacts svg { width: 13px; height: 13px; flex: none; }
  .address {
    position: absolute;
    right: 40px;
    top: 184px;
    font-size: 12.5px;
    font-style: normal;
    color: var(--ink-soft);
    line-height: 22px;
    white-space: nowrap;
  }

  /* Brand lockup */
  .brand {
    display: flex;
    align-items: center;
    gap: 12px;
  }
  .brand .mark {
    width: 26px;
    height: 26px;
    background: currentColor;
    flex: none;
  }
  .brand .divider {
    width: 1px;
    height: 50px;
    background: currentColor;
  }
  .brand .wordmark {
    font-weight: 600;
    font-size: 16px;
    letter-spacing: 0.6px;
    line-height: 1.15;
    text-transform: uppercase;
  }

  /* Back */
  .card-back {
    background: var(--card-black);
    color: var(--paper-text);
    display: flex;
    align-items: center;
    justify-content: center;
  }
  .card-back .brand { gap: 18px; }
  .card-back .brand .mark { width: 36px; height: 36px; }
  .card-back .brand .divider { height: 72px; }
  .card-back .brand .wordmark { font-size: 22px; }
</style>
</head>
<body>
<main class="stage">
  <section class="card card-front" aria-label="Business card front">
    <div class="brand front-brand">
      <span class="mark" aria-hidden="true"></span>
      <span class="divider" aria-hidden="true"></span>
      <span class="wordmark">Veridan Strategy<br>Group</span>
    </div>

    <div class="identity">
      <p class="name">Dr. Tomas Ruelle-Brandt</p>
      <p class="role">Principal Advisor</p>
    </div>

    <div class="rule" aria-hidden="true"></div>

    <ul class="contacts">
      <li>
        <svg viewBox="0 0 16 16" aria-hidden="true"><path d="M3.6 1.5l2.3 2.6-1.3 1.6c.9 2 2.3 3.4 4.3 4.3l1.6-1.3 2.6 2.3-1.4 2.3C6.6 13 3 9.4 1.7 4.3z" fill="#111"/></svg>
        <span>1234567890</span>
      </li>
      <li>
        <svg viewBox="0 0 16 16" aria-hidden="true"><rect x="1" y="3" width="14" height="10" fill="#111"/><path d="M1.5 3.5L8 9l6.5-5.5" stroke="#fff" stroke-width="1.2" fill="none"/></svg>
        <span>TRB@VeridanStrategy.com</span>
      </li>
      <li>
        <svg viewBox="0 0 16 16" aria-hidden="true"><circle cx="8" cy="8" r="7" fill="#111"/><g stroke="#fff" stroke-width="0.8" fill="none"><ellipse cx="8" cy="8" rx="3" ry="5.5"/><path d="M2.5 8h11M3.5 5h9M3.5 11h9"/></g></svg>
        <span>www.veridanstrategy.com</span>
      </li>
    </ul>

    <address class="address">
      1234 First Line Address<br>
      5678 Second Line Address
    </address>
  </section>

  <section class="card card-back" aria-label="Business card back">
    <div class="brand">
      <span class="mark" aria-hidden="true"></span>
      <span class="divider" aria-hidden="true"></span>
      <span class="wordmark">Veridan Strategy<br>Group</span>
    </div>
  </section>
</main>
</body>
</html>
```